I need a label with logo to go on jars of honey.
Label size 70mm x 70mm
The front label should say :
The Tall Fern Honey Co. (logo)
Tarepo Honey
400g
The back label:
Would have nutritional information
And our address
You can see from the uploaded files the styles I prefer, I have uploaded a photo of the honey product too. The background of the logo doesn't have to be white. I would like to develop a color scheme that would look nice against the color of the honey.
Logo Text
The Tall Fern Honey Co. / The Tall Fern Honey Company

```html
<!DOCTYPE html>
<html lang="en">
<head>
<meta charset="utf-8">
<title>Tarepo Honey – Jar Labels</title>
<link href="https://fonts.googleapis.com/css2?family=Anton&family=Archivo+Black&family=Arimo:wght@400;700&family=Barlow+Condensed:wght@500&family=Kaushan+Script&display=swap" rel="stylesheet">
<style>
  :root{
    --stage:#202020;
    --ink:#222222;
    --ink-soft:#353535;
    --amber:#f7a51c;
    --amber-deep:#ee8a12;
    --honey-pale:#fdf0b8;
    --honey-mid:#fcd867;
    --orange-brand:#e4572e;
    --script-top:#f19a2c;
    --script-bottom:#d9521c;
    --white:#ffffff;
  }
  *{box-sizing:border-box;margin:0;padding:0}
  html,body{width:1200px;height:719px;overflow:hidden;background:var(--stage)}
  .stage{position:relative;width:1200px;height:719px;background:var(--stage)}

  .label{
    position:absolute;top:125px;width:469px;height:469px;overflow:hidden;
    background:radial-gradient(ellipse at 60% 45%, var(--honey-pale) 0%, #fbe7a0 40%, var(--honey-mid) 75%, var(--amber) 100%);
    box-shadow:6px 10px 18px rgba(0,0,0,.55);
  }
  .label--front{left:140px}
  .label--back{left:622px}

  .top-band{position:absolute;left:0;top:0;width:100%;height:48px;
    background:linear-gradient(90deg,#f9e04b,var(--amber) 60%,var(--amber-deep))}
  .top-band::after{content:"";position:absolute;left:0;right:0;top:27px;height:8px;background:#fde3a2}

  .art{position:absolute}
  .art--dipper{left:0;top:0;width:200px;height:165px;
    background:radial-gradient(ellipse at 40% 40%, #fbd36a 0%, #f0a43a 55%, rgba(230,140,50,0) 80%)}
  .art--drip{right:0;top:0;width:210px;height:112px;
    background:radial-gradient(ellipse at 50% 30%, #fff2a8 0%, #f9d150 55%, rgba(245,175,40,0) 85%)}
  .art--comb{left:0;bottom:0;width:200px;height:215px;
    background:radial-gradient(ellipse at 35% 55%, #fde68a 0%, #f9c23c 55%, rgba(240,150,30,0) 90%)}
  .art--hexband{left:0;top:296px;width:100%;height:90px;
    background:linear-gradient(180deg, rgba(246,190,120,0) 0%, rgba(244,176,104,.55) 60%, rgba(240,160,90,.7) 100%)}

  .bottom-band{position:absolute;left:0;bottom:0;width:100%;height:83px;background:var(--amber)}

  .brand{position:absolute;left:167px;top:66px;width:140px;text-align:center;
    font-family:"Arimo",sans-serif;font-weight:700;font-size:15px;line-height:18px;color:var(--orange-brand)}

  .product-name{position:absolute;left:0;top:0;width:469px;height:469px}
  .product-name__main{font-family:"Anton",sans-serif;fill:var(--ink)}
  .product-name__sub{font-family:"Kaushan Script",cursive;font-size:84px;
    fill:url(#scriptFill);stroke:var(--white);stroke-width:6px;paint-order:stroke}

  .weight{position:absolute;left:192px;top:405px;
    font-family:"Archivo Black",sans-serif;font-size:30px;color:var(--ink-soft);letter-spacing:.5px}

  .nutrition{position:absolute;left:32px;top:44px;width:404px;height:228px;
    background:var(--white);border:7px solid #000;padding:6px 13px 0 13px;
    font-family:"Arimo",sans-serif;font-weight:700;color:#111}
  .nutrition__title{font-family:"Archivo Black",sans-serif;font-size:32px;line-height:34px;margin-left:4px;letter-spacing:.3px}
  .nutrition__serving{font-size:13px;line-height:14px;margin-left:4px}
  .nutrition__row{display:flex;justify-content:space-between;align-items:center;
    font-size:13px;padding:0 4px;border-top:1px solid #222;height:25px}
  .nutrition__row--thick{border-top:4px solid #000}
  .nutrition__row--dv{justify-content:flex-end;font-size:12.5px;height:28px}
  .nutrition__serving + .nutrition__row{margin-top:8px}

  .blurb{position:absolute;left:36px;top:283px;width:397px;text-align:center;
    font-family:"Arimo",sans-serif;font-size:13.3px;line-height:19.6px;color:var(--ink-soft)}

  .contact{position:absolute;left:0;top:402px;width:100%;text-align:center;
    font-family:"Barlow Condensed",sans-serif;font-weight:500;font-size:23px;line-height:25px;color:#3a3530}
</style>
</head>
<body>
<main class="stage">

  <section class="label label--front">
    <div class="top-band"></div>
    <div class="art art--dipper" role="img" aria-label="Honey dipper dripping honey with a bee"></div>
    <div class="art art--drip" role="img" aria-label="Glossy honey dripping from the top edge"></div>
    <div class="art art--hexband" role="img" aria-label="Honeycomb hexagon pattern"></div>
    <div class="art art--comb" role="img" aria-label="Golden honeycomb pieces"></div>
    <div class="bottom-band"></div>

    <div class="brand">The Tall Fern<br>Honey Co.</div>

    <svg class="product-name" viewBox="0 0 469 469" aria-label="Tarepo Honey">
      <defs>
        <linearGradient id="scriptFill" x1="0" y1="0" x2="0" y2="1">
          <stop offset="0" stop-color="var(--script-top)"/>
          <stop offset="1" stop-color="var(--script-bottom)"/>
        </linearGradient>
      </defs>
      <text class="product-name__main" x="53" y="270" font-size="150" textLength="363" lengthAdjust="spacingAndGlyphs">TAREPO</text>
      <text class="product-name__sub" x="318" y="330" text-anchor="middle" transform="rotate(-20 318 310)">Honey</text>
    </svg>

    <div class="weight">400G</div>
  </section>

  <section class="label label--back">
    <div class="top-band"></div>
    <div class="art art--drip" role="img" aria-label="Glossy honey dripping from the top edge"></div>
    <div class="art art--hexband" role="img" aria-label="Honeycomb hexagon pattern"></div>
    <div class="bottom-band"></div>

    <div class="nutrition">
      <div class="nutrition__title">Nutrition Facts</div>
      <div class="nutrition__serving">Serving Size 1tbsp (21g)</div>
      <div class="nutrition__row nutrition__row--thick"><span>Amount Per Srving</span></div>
      <div class="nutrition__row"><span>Calories 64</span></div>
      <div class="nutrition__row nutrition__row--thick nutrition__row--dv"><span>%Daily Value*</span></div>
      <div class="nutrition__row"><span>Total Fat 0g</span><span>0%</span></div>
      <div class="nutrition__row"><span>Sodium 0mg</span><span>0%</span></div>
      <div class="nutrition__row"><span>Protein 0g</span><span>0%</span></div>
    </div>

    <p class="blurb">Lorem ipsum dolor sit amet, consectetuer adipiscing elit, sed diam nonummy nibh euismod tincidunt ut laoreet dolore magna aliquam erat volutpat. Ut wisi enim ad minim veniam,</p>

    <p class="contact">Address: your addres here please, address.<br>Ph: 01230004567 | web:thetallfernhoneyco.</p>
  </section>

</main>
</body>
</html>
```